International sourcing and trading company needs website design on Squarespace

We are international sourcing and trading company based in Brisbane ,Australia. We help our clients to source any products they need to economically produce overseas and we manage the whole production process for them. We want our visual identity to show that we are professional, dynamic, efficient and are able to source any product around the world. Our website will be simply information and advertising website , no ecommerce or any transactions. Please see attached our company logo. We would like our website to have the following sections/pages:

1.Main banner with a simple slogan/sentence to introduce what we do: Let us handle the overseas sourcing and production for you.

2. Post-Covid sourcing and producing management: introducing our competence on managing sourcing and overseas production under the travel restriction and the growing tension on global trading. We will supply the exact wording later on;

3. About us: We are a professional team with mature global sourcing and trading experience. We have branch office in Hong Kong and local resources around all areas in China , India and other Asian countries. Our working flow is: received inquiry->start sourcing->(in 1 week time)give price and delivery date on inquired products or further information->(if needed)arrange samples for clients->(if samples and orders are confirmed)deliver Pre-production sample-> kick-off production->arrange inspection through the whole production-> (if need) arrange shipment to client. We would like to show the work flow in a personalized way , eg. personalize icons etc.;

4. What kind of product we can source and produce: our business is sourcing and managing manufacture overseas for our clients, product categories mainly, but not just, are clothing, shoes , bags, clothing accessories, makeup accessories, festival or promotional gifts etc. all kind of daily use products . We basically are able to source and manage production of every kind of products with no limits. We would like this page to be particularly personalized in a way to give impression to whom browse our website feel free to send inquiry of any kind of production to us and they can trust us that we will do our job professionally and dynamically. We are thinking of using some icons of daily use products to show our sourcing category , it's just our though so please feel free to propose any other ides that you think is more suitable from the point of view of professional designer.

5. Start an enquiry: here we need to land on a questionary page to let who would like to make en enquiry leave the main information , including:
-Name & Sir name:
-Company name:
-Contact email:
-Phone numer:
-Enquired product:
-Upload image:
-Preferred or previous production country:
-Preferred price: FOB, CIF, DDP
-If CIF or DDP where the arrival port/airport will be:
-Preferred delivery time:
-Preferred transportation: by air, by sea, by train
- Other specific requires:

6: Contact us: We will supply contact info later on

Above are our thoughts but please feel free to propose any other ideas that you think should be more suitable for us. We trust your expertise and professional opinions.

Wholesalers and retailers who need to produce their products overseas (mainly in China and other countries in Asia)

Coded - Design and coding required

Sans Serif

• We think it will be nice to show information in simple and comprehensive icons instead of piles of words. We will want our website neat, easy to understand what we do and professional. However this is just our thought so please feel free to propose any other ideas that you think is more suitable from the point of view of professional designer.

```html
<!DOCTYPE html>
<html lang="en">
<head>
<meta charset="utf-8">
<title>Crestway – Global sourcing and trading</title>
<link href="https://fonts.googleapis.com/css2?family=Heebo:wght@300;400;500;700&family=Poppins:wght@700;800&display=swap" rel="stylesheet">
<style>
:root{
  --orange:#f7a03c;
  --orange-dark:#f08a1c;
  --teal:#40acc3;
  --teal-deep:#2f9fbc;
  --ink:#1c1c1c;
  --text:#333;
  --muted:#f3f1f1;
  --ring:#c9cfd1;
  --footer:#232323;
  --white:#fff;
}
*{box-sizing:border-box;margin:0;padding:0}
html,body{width:1200px;height:3050px;overflow:hidden}
body{font-family:"Heebo",Arial,sans-serif;color:var(--text);background:var(--white)}
.page{position:relative;width:1200px;height:3050px}

/* notice */
.notice{height:45px;background:var(--orange);color:var(--white);font-size:13px;line-height:16px;text-align:center;padding-top:6px}

/* header */
.site-header{position:relative;height:100px}
.brand{position:absolute;left:131px;top:28px;display:flex;align-items:center;gap:10px}
.brand-dot{width:34px;height:34px;border-radius:50%;background:var(--orange)}
.brand-name{font-size:28px;font-weight:500;color:var(--orange)}
.follow{position:absolute;right:130px;top:20px;display:flex;align-items:center;gap:8px;font-size:11px;color:var(--ink)}
.follow span.social{width:27px;height:27px;border-radius:50%;display:block}
.s1{background:#3b5ea8}.s2{background:#2fa6e4}.s3{background:#1b2e6b}
.nav{position:absolute;right:130px;top:68px;display:flex;gap:41px;font-size:15px;font-weight:500;color:var(--ink)}
.nav .active{color:var(--orange);text-decoration:underline;text-underline-offset:4px}

/* hero */
.hero{position:relative;height:573px;background:linear-gradient(135deg,#283c5c 0%,#5b7594 35%,#a9b5c2 50%,#4e6785 68%,#1f3150 100%);overflow:hidden}
.hero-title{position:absolute;top:390px;left:0;width:100%;text-align:center;font-family:"Poppins",Arial,sans-serif;font-weight:800;font-size:27px;line-height:35px;color:var(--white);text-shadow:0 2px 6px rgba(0,0,0,.45)}
.btn{display:inline-block;background:var(--orange);color:var(--white);font-weight:700;text-transform:uppercase;text-align:center}
.hero .btn{position:absolute;left:531px;top:482px;width:137px;height:36px;line-height:36px;font-family:"Poppins",Arial,sans-serif;font-size:15px}
.slide-arrow{position:absolute;top:270px;width:29px;height:29px;background:var(--teal)}
.slide-arrow.prev{left:0}.slide-arrow.next{right:0}
.slide-arrow svg{display:block}

/* section heading */
.section-title{text-align:center;font-size:26px;font-weight:500;color:var(--ink);letter-spacing:.3px}
.rule{width:40px;height:2px;background:var(--teal);margin:0 auto}

/* categories */
.categories{height:565px;padding-top:44px}
.categories .rule{margin-top:14px}
.cat-grid{position:absolute;left:138px;top:838px;display:grid;grid-template-columns:298px 298px 298px;grid-auto-rows:187px;column-gap:15px;row-gap:13px}
.cat-tile{background:var(--teal);color:var(--white);display:flex;flex-direction:column;align-items:center;justify-content:flex-start;padding-top:34px;text-align:center;font-size:16px;font-weight:500;letter-spacing:.5px;text-transform:uppercase}
.cat-tile svg{width:86px;height:80px;margin-bottom:22px}
.cat-tile.two-line{padding-top:32px}
.cat-tile.two-line svg{margin-bottom:18px}
.cat-tile p{line-height:22px}

/* workflow */
.welcome{position:relative;height:794px;background:var(--muted);padding-top:44px;overflow:hidden}
.welcome .section-title{font-size:24px}
.welcome .lead{width:560px;margin:14px auto 0;text-align:center;font-size:18px;line-height:25.5px;color:var(--ink);font-weight:300}
.welcome .rule{margin-top:26px}
.flow{position:absolute;left:0;top:0;width:1200px;height:794px}
.hub{position:absolute;left:443px;top:231px;width:320px;height:320px;border-radius:50%;background:var(--white);box-shadow:0 10px 30px rgba(0,0,0,.18);display:flex;align-items:center;justify-content:center;gap:12px}
.hub-dot{width:30px;height:30px;border-radius:50%;background:var(--teal)}
.hub-name{font-size:34px;font-weight:500;color:var(--teal)}
.step{position:absolute;font-size:15px;line-height:20px;color:var(--ink);font-weight:300}
.step.r{text-align:right}
.step.c{text-align:center}

/* enquiry */
.enquiry{position:relative;height:629px;background:linear-gradient(180deg,#35a9c5 0%,#3cafca 55%,#2f9fbe 100%)}
.enquiry .section-title{color:var(--white);padding-top:38px;font-weight:700;font-size:24px}
.enquiry .rule{background:var(--white);margin-top:12px}
.field{position:absolute;background:var(--white);height:43px;font-size:14px;color:var(--ink);padding:0 17px;display:flex;align-items:center}
.field.l{left:240px;width:352px}.field.rt{left:605px;width:352px}
.field.select{justify-content:space-between}
.field .stack{display:flex;flex-direction:column;line-height:15px}
.field .stack small{font-size:9.5px}
.field.upload{padding-right:0}
.upload-btn{margin-left:auto;height:43px;width:110px;background:var(--orange);color:var(--white);font-weight:700;font-size:16px;display:flex;align-items:center;justify-content:center;gap:7px}
.field.area{left:240px;width:718px;height:130px;align-items:flex-start;padding-top:14px}
.enquiry .btn{position:absolute;left:541px;top:546px;width:119px;height:42px;line-height:42px;font-size:16px;border:2px solid var(--white)}

/* footer */
.site-footer{position:relative;height:344px;background:var(--footer);color:var(--white)}
.foot-brand{position:absolute;left:135px;top:90px;display:flex;align-items:center;gap:12px}
.foot-brand .brand-dot{background:var(--white);width:40px;height:40px}
.foot-brand .brand-name{color:var(--white);font-size:44px}
.foot-col{position:absolute;top:50px;font-size:12px;line-height:15px}
.foot-col h4{font-size:13px;font-weight:700;letter-spacing:.5px;margin-bottom:22px}
.foot-menu li{list-style:none;margin-bottom:16px}
.contact-item{display:flex;gap:12px;align-items:center;margin-bottom:26px}
.contact-item .ico{width:24px;height:24px;border-radius:50%;background:var(--white);flex:none;display:flex;align-items:center;justify-content:center}
.foot-rule{position:absolute;left:135px;right:135px;top:262px;height:1px;background:#3c3c3c}
.copyright{position:absolute;top:307px;width:100%;text-align:center;font-size:10px}
</style>
</head>
<body>
<div class="page">

  <div class="notice">Post-Covid sourcing and producing management: introducing our competence on managing sourcing and overseas production under<br>the travel restriction and the growing tension on global trading. We will supply the exact wording later on</div>

  <header class="site-header">
    <div class="brand"><span class="brand-dot"></span><span class="brand-name">Crestway</span></div>
    <div class="follow">FOLLOW <span class="social s1"></span><span class="social s2"></span><span class="social s3"></span></div>
    <nav class="nav"><span class="active">HOME</span><span>ABOUT US</span><span>CATEGORIES</span><span>CONTACT US</span></nav>
  </header>

  <section class="hero" role="img" aria-label="Business partners stacking hands over a city skyline with a dotted world map overlay">
    <span class="slide-arrow prev"><svg width="29" height="29" viewBox="0 0 29 29"><path d="M17 9l-5 5.5 5 5.5" fill="none" stroke="#fff" stroke-width="2"/></svg></span>
    <span class="slide-arrow next"><svg width="29" height="29" viewBox="0 0 29 29"><path d="M12 9l5 5.5-5 5.5" fill="none" stroke="#fff" stroke-width="2"/></svg></span>
    <h1 class="hero-title">LET US HANDLE THE OVERSEAS SOURCING<br>AND PRODUCTION FOR YOU.</h1>
    <span class="btn">Read more</span>
  </section>

  <section class="categories">
    <h2 class="section-title">CATEGORIES</h2>
    <div class="rule"></div>
    <div class="cat-grid">
      <div class="cat-tile">
        <svg viewBox="0 0 86 80"><path d="M30 4l-22 12 6 20 8-4v44h42V32l8 4 6-20L56 4c-2 7-7 10-13 10S32 11 30 4z" fill="#fff"/><path d="M43 14v62" stroke="#40acc3" stroke-width="1.5"/></svg>
        <p>Clothing</p>
      </div>
      <div class="cat-tile">
        <svg viewBox="0 0 86 80"><path d="M12 6h26v30c8 4 20 8 30 12 6 2 8 7 8 12H12z" fill="#fff"/><rect x="12" y="62" width="64" height="8" fill="#fff"/><path d="M38 18h-8M38 26h-8" stroke="#40acc3" stroke-width="2"/></svg>
        <p>Shoes</p>
      </div>
      <div class="cat-tile">
        <svg viewBox="0 0 86 80"><path d="M28 30V20a15 15 0 0130 0v10" fill="none" stroke="#fff" stroke-width="5"/><path d="M14 32h58l6 40H8z" fill="#fff"/><circle cx="43" cy="42" r="4" fill="#40acc3"/></svg>
        <p>Bags</p>
      </div>
      <div class="cat-tile">
        <svg viewBox="0 0 86 80"><circle cx="43" cy="22" r="17" fill="#fff"/><path d="M22 34h14v40l-7-4-7 4zM50 34h14v36l-7 4-7-4z" fill="#fff"/></svg>
        <p>Clothing accessories</p>
      </div>
      <div class="cat-tile">
        <svg viewBox="0 0 86 80"><circle cx="34" cy="22" r="18" fill="none" stroke="#fff" stroke-width="4"/><ellipse cx="34" cy="58" rx="24" ry="12" fill="#fff"/><path d="M64 40h10v34H64z" fill="#fff"/><path d="M62 40l7-14 7 14z" fill="#fff"/></svg>
        <p>Makeup accessories</p>
      </div>
      <div class="cat-tile two-line">
        <svg viewBox="0 0 86 80"><rect x="14" y="22" width="58" height="14" fill="#fff"/><rect x="18" y="40" width="50" height="36" fill="#fff"/><path d="M43 22c-6-14-20-14-18-4 1 4 10 4 18 4zm0 0c6-14 20-14 18-4-1 4-10 4-18 4z" fill="none" stroke="#fff" stroke-width="4"/><path d="M40 22h6v54h-6z" fill="#40acc3"/></svg>
        <p>Festival or<br>promotional gifts</p>
      </div>
    </div>
  </section>

  <section class="welcome">
    <h2 class="section-title">WELCOME TO CRESTWAY</h2>
    <p class="lead">We are a professional team with mature global sourcing and trading experience. We have branch office in Hong Kong and local resources around all areas in China , India and other Asian countries.</p>
    <div class="rule"></div>

    <svg class="flow" viewBox="0 0 1200 794" aria-hidden="true">
      <path d="M421 288 A209 209 0 1 0 787 288" fill="none" stroke="var(--ring)" stroke-width="6"/>
      <g fill="#fff" stroke="var(--teal)" stroke-width="3.5">
        <circle cx="421" cy="288" r="13"/><circle cx="392" cy="417" r="13"/><circle cx="442" cy="527" r="13"/><circle cx="544" cy="592" r="13"/>
        <circle cx="667" cy="592" r="13"/><circle cx="764" cy="527" r="13"/><circle cx="812" cy="417" r="13"/><circle cx="787" cy="288" r="13"/>
      </g>
      <g fill="var(--orange)" stroke="#f7c17f" stroke-width="1.5" stroke-dasharray="2 2">
        <circle cx="349" cy="295" r="39"/><circle cx="328" cy="432" r="39"/><circle cx="393" cy="566" r="39"/><circle cx="529" cy="657" r="39"/>
        <circle cx="691" cy="657" r="39"/><circle cx="815" cy="566" r="39"/><circle cx="877" cy="432" r="39"/><circle cx="853" cy="295" r="39"/>
      </g>
      <g fill="none" stroke="#fff" stroke-width="3" stroke-linejoin="round" stroke-linecap="round">
        <rect x="335" y="281" width="26" height="26" rx="2"/><path d="M343 300l3-8 12-12 5 5-12 12z"/>
        <path d="M328 412c8 8 8 22 4 30h-8c-4-8-4-22 4-30zM320 438l-6 8M336 438l6 8M328 446v8"/><circle cx="328" cy="426" r="3"/>
        <rect x="380" y="551" width="22" height="30" rx="2"/><path d="M385 561h10M385 568h12M385 575h8"/><circle cx="404" cy="556" r="7"/>
        <circle cx="519" cy="644" r="5"/><circle cx="539" cy="644" r="5"/><path d="M512 672v-14h14v14M532 672v-14h14v14"/>
        <rect x="677" y="643" width="26" height="18"/><path d="M685 668h10M690 661v7"/><path d="M683 652l5-4 5 4"/>
        <path d="M800 582v-18l8-5v5l8-5v5l8-5v23zM804 546h4v13"/>
        <rect x="864" y="418" width="20" height="28"/><path d="M868 426h10M868 433h8"/><circle cx="887" cy="440" r="6"/><path d="M891 444l4 4"/>
        <rect x="836" y="284" width="20" height="18"/><path d="M856 290h8l6 6v6h-14z"/><circle cx="843" cy="306" r="3"/><circle cx="863" cy="306" r="3"/>
      </g>
    </svg>

    <div class="hub"><span class="hub-dot"></span><span class="hub-name">Crestway</span></div>

    <p class="step r" style="right:906px;top:272px">Received<br>Inquiry</p>
    <p class="step r" style="right:922px;top:421px">Start Sourcing</p>
    <p class="step r" style="right:861px;top:544px">Give price and delivery date<br>on inquired products or<br>further information</p>
    <p class="step c" style="left:459px;top:711px;width:126px">Arrange samples<br>for clients</p>
    <p class="step c" style="left:619px;top:711px;width:140px">Deliver Pre-<br>production sample</p>
    <p class="step" style="left:868px;top:549px">kick- off<br>production</p>
    <p class="step" style="left:927px;top:413px">Arrange inspection through<br>the whole production</p>
    <p class="step" style="left:904px;top:275px">Arrange shipment<br>to client.</p>
  </section>

  <section class="enquiry" role="img" aria-label="Teal-tinted city skyline behind the enquiry form">
    <h2 class="section-title">ENQUIRY</h2>
    <div class="rule"></div>
    <div class="field l" style="top:114px">Name</div>
    <div class="field rt" style="top:114px">Company Name</div>
    <div class="field l" style="top:170px">E mail</div>
    <div class="field rt" style="top:170px">Phone numer</div>
    <div class="field l" style="top:225px">Enquired product</div>
    <div class="field rt upload" style="top:225px">Upload image
      <span class="upload-btn"><svg width="14" height="14" viewBox="0 0 14 14"><path d="M7 1v8M3 5l4-4 4 4M1 13h12" fill="none" stroke="#fff" stroke-width="2"/></svg>UPLOAD</span>
    </div>
    <div class="field l select" style="top:281px">Preferred or previous production country
      <svg width="12" height="8" viewBox="0 0 12 8"><path d="M1 1l5 5 5-5" fill="none" stroke="#222" stroke-width="1.6"/></svg></div>
    <div class="field rt select" style="top:281px"><span class="stack"><small>If CIF or DDP where the arrival port/airport will be</small>Preferred price</span>
      <svg width="12" height="8" viewBox="0 0 12 8"><path d="M1 1l5 5 5-5" fill="none" stroke="#222" stroke-width="1.6"/></svg></div>
    <div class="field l select" style="top:335px">Preferred delivery time
      <svg width="12" height="8" viewBox="0 0 12 8"><path d="M1 1l5 5 5-5" fill="none" stroke="#222" stroke-width="1.6"/></svg></div>
    <div class="field rt select" style="top:335px">Preferred transportation
      <svg width="12" height="8" viewBox="0 0 12 8"><path d="M1 1l5 5 5-5" fill="none" stroke="#222" stroke-width="1.6"/></svg></div>
    <div class="field area" style="top:390px">Other specific requires</div>
    <span class="btn">Submit</span>
  </section>

  <footer class="site-footer">
    <div class="foot-brand"><span class="brand-dot"></span><span class="brand-name">Crestway</span></div>
    <div class="foot-col" style="left:497px">
      <h4>MENU</h4>
      <ul class="foot-menu"><li>HOME</li><li>ABOUT US</li><li>CATEGORIES</li><li>CONTACT US</li></ul>
    </div>
    <div class="foot-col" style="left:690px">
      <h4>CONTACT US</h4>
      <div class="contact-item"><span class="ico"><svg width="12" height="14" viewBox="0 0 12 14"><path d="M6 13S1 8 1 5a5 5 0 0110 0c0 3-5 8-5 8z" fill="#232323"/><circle cx="6" cy="5" r="1.8" fill="#fff"/></svg></span><span>2250 Harlow Street<br>Fenwick, CA 90412</span></div>
      <div class="contact-item"><span class="ico"><svg width="12" height="12" viewBox="0 0 12 12"><path d="M2 1l3 1 1 3-2 1c1 2 2 3 4 4l1-2 3 1 0 3c-6 0-10-5-10-11z" fill="#232323"/></svg></span><span>Call Us<br>555.010.0199</span></div>
      <div class="contact-item"><span class="ico"><svg width="12" height="10" viewBox="0 0 12 10"><rect x="0.5" y="0.5" width="11" height="9" fill="#232323"/><path d="M1 1l5 4 5-4" fill="none" stroke="#fff"/></svg></span><span>E mail Us<br>hello@crestway.example</span></div>
    </div>
    <div class="foot-col" style="left:965px">
      <h4>FOLLOW US</h4>
      <div class="contact-item"><span class="ico"></span><span>Like us on<br>FRIENDNET</span></div>
      <div class="contact-item"><span class="ico"></span><span>Follow us on<br>CHIRPER</span></div>
      <div class="contact-item"><span class="ico"></span><span>Follow us on<br>WORKLINK</span></div>
    </div>
    <div class="foot-rule"></div>
    <p class="copyright">Copyright © 2020 All Rights Reserved</p>
  </footer>

</div>
</body>
</html>
```